Small rum distillery looking for bottle design

Small rum distillery in Estonia. Looking for bottle lable design. It should be simple but at the same time point out from the variety of other bottles.
As we are a small nordic country, design can be some how nordic or represent our country. It can also have some connection with sailing or sea as we know it pirates love it.
Bottle we are using is Corvane 540

Industry/Entity Type

food and beverage

Other font styles liked:
• Baskerville

```html
<!DOCTYPE html>
<html lang="en">
<head>
<meta charset="utf-8">
<title>Halvik Liqueur – Bottle Label</title>
<link href="https://fonts.googleapis.com/css2?family=Cormorant+Garamond:wght@400;500&family=Libre+Baskerville&family=Oswald:wght@300&display=swap" rel="stylesheet">
<style>
  :root {
    --backdrop: #e4e4e4;
    --label-paper: #ededed;
    --navy: #1f4a9c;
    --ink: #5a5a5a;
    --rule: #9a9a9a;
    --edge: #c9c9c9;
  }
  * { margin: 0; padding: 0; box-sizing: border-box; }
  html, body {
    width: 1200px; height: 875px; overflow: hidden;
    background: var(--backdrop);
  }
  .stage { position: relative; width: 1200px; height: 875px; }

  .label {
    position: absolute; left: 330px; top: 50px;
    width: 540px; height: 752px;
    background: var(--label-paper);
    color: var(--ink);
    font-family: "Libre Baskerville", "Baskerville", serif;
  }
  .label-edge { position: absolute; left: 0; bottom: -8px; width: 540px; height: 12px; }

  .emblem { position: absolute; left: 45px; top: 82px; width: 450px; height: 450px; }

  .anchor-mark {
    position: absolute; left: 252px; top: 160px; width: 36px; height: 52px;
  }

  .brand-name {
    position: absolute; left: 0; width: 540px; top: 250px;
    text-align: center;
    font-family: "Cormorant Garamond", "Libre Baskerville", serif;
    font-weight: 500; font-size: 68px; letter-spacing: 4px;
  }
  .product-kind {
    position: absolute; left: 0; width: 540px; top: 338px;
    text-align: center;
    font-family: "Cormorant Garamond", serif;
    font-weight: 500; font-size: 27px; letter-spacing: 3px;
  }

  .rule { position: absolute; left: 12px; width: 516px; height: 1px; background: var(--rule); }
  .rule-top { top: 637px; }
  .rule-bottom { top: 686px; }

  .craft-row {
    position: absolute; left: 12px; width: 516px; top: 652px;
    display: flex; justify-content: space-between; align-items: center;
    font-size: 14px; letter-spacing: 3px;
  }
  .craft-mark {
    display: flex; align-items: center; gap: 6px;
    font-size: 14px; letter-spacing: 2px;
  }
  .craft-mark::before {
    content: ""; width: 14px; height: 14px; border: 1px solid var(--ink); border-radius: 50%;
  }

  .spec-row {
    position: absolute; left: 12px; width: 516px; top: 696px; height: 40px;
    display: flex; align-items: center;
  }
  .spec-value {
    font-family: "Oswald", sans-serif; font-weight: 300; font-size: 24px;
    padding: 0 20px;
  }
  .spec-divider { width: 1px; height: 30px; background: var(--ink); }
  .producer {
    flex: 1; text-align: left; padding-left: 28px;
    font-size: 10.5px; letter-spacing: 1.5px; line-height: 1.45;
  }
</style>
</head>
<body>
<main class="stage">
  <section class="label">
    <svg class="emblem" viewBox="0 0 450 450" role="img" aria-label="Woven rope ring pattern in navy around the label centre">
      <circle cx="225" cy="225" r="205" fill="none" stroke="var(--navy)" stroke-width="38"/>
    </svg>

    <svg class="anchor-mark" viewBox="0 0 36 52" role="img" aria-label="Small navy anchor illustration">
      <rect x="0" y="0" width="36" height="52" rx="6" fill="var(--navy)" opacity="0.85"/>
    </svg>

    <h1 class="brand-name">HALVIK</h1>
    <p class="product-kind">LIQUEUR</p>

    <div class="rule rule-top"></div>
    <div class="craft-row">
      <span>HANDCRAFTED</span>
      <span class="craft-mark">HALVIK</span>
      <span>SMALL BATCH</span>
    </div>
    <div class="rule rule-bottom"></div>

    <div class="spec-row">
      <span class="spec-value">40%</span>
      <span class="spec-divider"></span>
      <p class="producer">PRODUCED AND BOTTLED BY<br>HALVIK DISTILLERY · ESTONIA</p>
      <span class="spec-divider"></span>
      <span class="spec-value">70 cl</span>
    </div>

    <svg class="label-edge" viewBox="0 0 540 12" preserveAspectRatio="none">
      <polygon fill="var(--label-paper)" points="0,0 540,0 540,4 531,10 522,4 513,10 504,4 495,10 486,4 477,10 468,4 459,10 450,4 441,10 432,4 423,10 414,4 405,10 396,4 387,10 378,4 369,10 360,4 351,10 342,4 333,10 324,4 315,10 306,4 297,10 288,4 279,10 270,4 261,10 252,4 243,10 234,4 225,10 216,4 207,10 198,4 189,10 180,4 171,10 162,4 153,10 144,4 135,10 126,4 117,10 108,4 99,10 90,4 81,10 72,4 63,10 54,4 45,10 36,4 27,10 18,4 9,10 0,4"/>
    </svg>
  </section>
</main>
</body>
</html>
```